Veltana corporate website

Dear graphic designers,
We would like to create a brand new corporate website for our company named "Veltana".
Veltana is a small Swiss premium IT company, with very prestigious clients in the Private Banking industry.
Here would be the values which could be associated to Veltana: trustworthy, serious, modern, high tech, high quality, sobriety, elegant.
Please find attached the Veltana logo in SVG format.
Our new website will have for only purpose to present briefly the company in one page: the team of experts (4 employees), the mission, the expertise and the contact info.
Very short and concise, easy to read.
Like this website for example but even shorter: https://www.dorimel-example.com/

```html
<!DOCTYPE html>
<html lang="en">
<head>
<meta charset="utf-8">
<title>Veltana — Trusted IT Solutions for Private Banking</title>
<link href="https://fonts.googleapis.com/css2?family=Figtree:wght@400;500;600;700;800&display=swap" rel="stylesheet">
<style>
:root{
  --blue:#0f4fa8;
  --blue-bright:#1a6fd8;
  --title-blue:#1457b0;
  --ink:#17202e;
  --text:#3b4150;
  --muted:#5c6473;
  --pale:#eef4fc;
  --navy:#0b1d48;
  --band:#1d3d78;
  --white:#ffffff;
  --line:#dfe6f0;
}
*{margin:0;padding:0;box-sizing:border-box}
html,body{width:1200px;height:3734px;overflow:hidden}
body{font-family:"Figtree",Arial,sans-serif;color:var(--text);background:var(--white);position:relative}
.abs{position:absolute}
section,header,footer{position:relative;width:1200px}
.eyebrow{font-size:12px;font-weight:700;letter-spacing:1px;color:var(--blue-bright);text-transform:uppercase}
.heading{font-size:26px;font-weight:600;color:var(--ink)}
.btn{position:absolute;display:flex;align-items:center;justify-content:center;background:var(--blue);color:var(--white);font-size:12px;font-weight:700;border-radius:22px;text-transform:uppercase;letter-spacing:.2px}
.brand{font-weight:600;color:var(--blue);letter-spacing:1px}

/* header */
.site-header{height:77px;background:var(--white)}
.site-header .brand{left:88px;top:18px;font-size:32px}
.nav{left:459px;top:30px;display:flex;font-size:13px;color:var(--ink)}
.nav span{margin-right:49px}
.site-header .btn{left:945px;top:19px;width:171px;height:41px}

/* hero */
.hero{height:558px}
.hero-photo{left:0;top:0;width:1200px;height:558px;background:linear-gradient(90deg,#f6f9fd 0%,#e8eef6 35%,#9fb2c9 60%,#7d8ea4 80%,#5d6e85 100%)}
.hero h1{left:87px;top:190px;font-size:40px;line-height:52px;font-weight:700;color:var(--title-blue)}
.hero p{left:87px;top:308px;width:420px;font-size:12.5px;line-height:21px;color:var(--ink)}
.hero .btn{left:87px;top:379px;width:171px;height:41px}

/* about */
.about{height:452px}
.about-photo{left:86px;top:40px}
.about .eyebrow{left:601px;top:56px}
.about .heading{left:601px;top:80px}
.about-copy{left:601px;top:128px;width:520px;font-size:13px;line-height:22.5px;color:var(--muted)}
.about-copy p+p{margin-top:22px}
.about .btn{left:599px;top:330px;width:153px;height:41px}

/* services */
.services{height:591px;background:var(--pale)}
.services .eyebrow{left:0;width:1200px;text-align:center;top:76px}
.services .heading{left:0;width:1200px;text-align:center;top:100px}
.service{position:absolute;width:330px}
.service svg{position:absolute;left:0;top:0}
.service h3{position:absolute;left:77px;top:0;font-size:14px;font-weight:700;color:var(--ink)}
.service p{position:absolute;left:77px;top:22px;width:225px;font-size:11.5px;line-height:17px;color:var(--text)}
.services .btn{left:505px;top:503px;width:171px;height:41px}

/* stats */
.stats{height:496px;background:linear-gradient(180deg,#1c3c78,#244a8c 50%,#1d3f7d)}
.stat{position:absolute;width:200px;text-align:center;color:var(--white)}
.stat svg{display:block;margin:0 auto}
.stat b{display:block;font-size:38px;font-weight:700;margin-top:6px;line-height:44px}
.stat span{display:block;font-size:12px;font-weight:700;margin-top:4px}
.stats-rule{left:101px;top:245px;width:1003px;height:1px;background:rgba(255,255,255,.25)}
.stats-cta{left:0;top:287px;width:1200px;text-align:center;color:var(--white);font-size:26px;font-weight:700;line-height:40px}

/* contact cards */
.contact-card{position:absolute;background:var(--white);box-shadow:0 8px 24px rgba(20,40,80,.12);height:171px;top:2087px}
.call{left:101px;width:481px}
.signup{left:624px;width:480px}
.call .label{left:135px;top:54px;font-size:13px;font-weight:600;color:var(--ink)}
.call .number{left:135px;top:76px;font-size:30px;font-weight:600;color:var(--ink)}
.signup .label{left:136px;top:43px;font-size:13px;font-weight:600;color:var(--ink)}
.field{left:136px;top:81px;width:260px;height:42px;border:1px solid var(--line);border-radius:3px;font-size:11px;color:var(--muted);padding:14px 18px;font-weight:600}
.field-btn{left:396px;top:81px;width:42px;height:42px;background:var(--blue);border-radius:3px;display:flex;align-items:center;justify-content:center}

/* team */
.team{position:absolute;top:2174px;height:644px;width:1200px}
.team .eyebrow{left:0;width:1200px;text-align:center;top:163px}
.team .heading{left:0;width:1200px;text-align:center;top:186px}
.member{position:absolute;top:252px;width:240px;text-align:center}
.portrait{width:232px;height:232px;margin:0 auto;border-radius:50%;background:radial-gradient(circle at 50% 40%,#f4f5f7 55%,#e6e9ee);box-shadow:0 4px 18px rgba(20,40,80,.12)}
.member h3{margin-top:22px;font-size:19px;font-weight:600;color:var(--title-blue)}
.member p{margin-top:6px;font-size:14px;font-weight:500;color:var(--ink)}
.socials{display:flex;justify-content:center;gap:18px;margin-top:16px}
.socials i{display:block;width:32px;height:32px;border-radius:50%;border:1px solid #cfd8e6;background:var(--white)}

/* testimonials */
.testimonials{position:absolute;top:2818px;height:474px;width:1200px}
.testimonials .eyebrow{left:100px;top:78px}
.testimonials .heading{left:100px;top:100px}
.arrow{position:absolute;top:90px;width:38px;height:37px;border:1px solid var(--line);display:flex;align-items:center;justify-content:center;background:var(--white)}
.quote{position:absolute;top:172px;height:130px;background:var(--white);box-shadow:0 6px 22px rgba(20,40,80,.1);padding:32px 34px;font-size:14px;line-height:26px;color:var(--ink)}
.author{position:absolute;top:326px;display:flex;align-items:center}
.avatar{width:76px;height:73px;border-radius:50%;background:linear-gradient(135deg,#c9d9ee,#8fa8c8)}
.author div{margin-left:22px}
.author b{display:block;font-size:14px;font-weight:600;color:var(--ink)}
.author small{display:block;font-size:10px;color:var(--blue-bright);margin-top:6px}

/* footer */
.site-footer{position:absolute;top:3292px;height:442px;width:1200px;background:var(--navy);color:#b9c4da}
.site-footer .brand{left:88px;top:28px;font-size:48px;color:#2a78e0}
.foot-social{top:38px;display:flex;gap:20px;right:112px}
.foot-social i{display:block;width:32px;height:32px;border-radius:50%;border:1px solid #2f6fd0}
.foot-rule{left:101px;width:1003px;height:1px;background:rgba(255,255,255,.12)}
.foot-col{position:absolute;top:166px}
.foot-col h4{font-size:13px;font-weight:700;color:var(--white);margin-bottom:22px}
.foot-col li{list-style:none;font-size:11.5px;line-height:27.5px}
.foot-col .contact li{line-height:22px;margin-bottom:10px;width:230px}
.foot-col a{color:#3f8ef0;text-decoration:none}
.copy{left:0;top:404px;width:1200px;text-align:center;font-size:11px}
</style>
</head>
<body>

<header class="site-header">
  <div class="abs brand">Veltana</div>
  <nav class="abs nav"><span>Home</span><span>Who we are</span><span>Services</span><span>Team</span><span>Contact us</span></nav>
  <a class="btn">Request a quote</a>
</header>

<section class="hero">
  <div class="abs hero-photo" role="img" aria-label="Photo of a business presentation in a glass-walled meeting room"></div>
  <h1 class="abs">Trusted IT Solutions<br>for Private Banking</h1>
  <p class="abs">Lorem Ipsum is simply dummy text of the printing and typesetting industry. Lorem Ipsum has been the industry's standard dummy text</p>
  <a class="btn">Contact now</a>
</section>

<section class="about">
  <svg class="abs about-photo" width="450" height="370" viewBox="0 0 450 370" role="img" aria-label="Photo of a team meeting around a conference table, framed in a speech bubble">
    <defs><linearGradient id="aboutFill" x1="0" y1="0" x2="1" y2="1"><stop offset="0" stop-color="#c7d4e4"/><stop offset=".55" stop-color="#8ea2bb"/><stop offset="1" stop-color="#5e7290"/></linearGradient></defs>
    <path d="M225 2C345 2 447 70 447 160c0 60-42 110-104 140l30 68-78-58c-23 5-46 8-70 8C103 318 2 248 2 160S103 2 225 2Z" fill="url(#aboutFill)"/>
  </svg>
  <div class="abs eyebrow">More about us</div>
  <h2 class="abs heading">Who we are</h2>
  <div class="abs about-copy">
    <p>Veltana is a Swiss-based IT company that specializes in providing cutting-edge solutions for the Private Banking industry. Founded in 2001, our team of experts has a combined experience of over 22 years in software development, cybersecurity, and data analytics.</p>
    <p>At Veltana, we believe that technology can be a powerful tool for enhancing the client experience in the Private Banking sector. Our mission is to provide our clients with the most innovative and effective IT solutions, tailored to their specific needs and goals.</p>
  </div>
  <a class="btn">More about us</a>
</section>

<section class="services">
  <div class="abs eyebrow">Bankig software service</div>
  <h2 class="abs heading">Our feature services</h2>

  <div class="service" style="left:103px;top:203px">
    <svg width="50" height="54" viewBox="0 0 50 54" fill="none" stroke="#1a5fc0" stroke-width="1.6"><rect x="3" y="4" width="44" height="38" rx="2"/><rect x="9" y="10" width="32" height="26"/><circle cx="25" cy="23" r="6"/><path d="M18 48h14M25 42v6"/></svg>
    <h3>Software Development</h3>
    <p>Veltana could highlight their expertise in developing custom software solutions for the Private Banking industry.</p>
  </div>
  <div class="service" style="left:470px;top:203px">
    <svg width="50" height="54" viewBox="0 0 50 54" fill="none" stroke="#1a5fc0" stroke-width="1.6"><rect x="3" y="10" width="44" height="30" rx="2"/><path d="M25 2l12 5v9c0 8-6 13-12 15-6-2-12-7-12-15V7z"/><rect x="20" y="15" width="10" height="8"/><path d="M18 48h14M25 40v8"/></svg>
    <h3>Cybersecurity</h3>
    <p>Veltana could showcase their cybersecurity services, which could include risk assessments, penetration testing, and vulnerability assessments.</p>
  </div>
  <div class="service" style="left:805px;top:203px">
    <svg width="56" height="54" viewBox="0 0 56 54" fill="none" stroke="#1a5fc0" stroke-width="1.6"><path d="M4 48V30h8v18M16 48V20h8v28M28 48V26h8v22"/><path d="M4 18l10-8 8 6 14-12"/><circle cx="44" cy="40" r="10"/><path d="M44 30v10h10"/></svg>
    <h3>Data Analytics</h3>
    <p>Veltana could highlight their experience in data analytics, including their ability to gather, process, and analyze large sets of data to provide insights and intelligence to their clients.</p>
  </div>

  <div class="service" style="left:103px;top:367px">
    <svg width="54" height="54" viewBox="0 0 54 54" fill="none" stroke="#1a5fc0" stroke-width="1.6"><rect x="28" y="4" width="22" height="14" rx="2"/><circle cx="28" cy="30" r="7"/><path d="M16 50c0-8 5-13 12-13s12 5 12 13"/><circle cx="10" cy="36" r="5"/><path d="M10 29v2M10 41v2M3 36h2M15 36h2"/></svg>
    <h3>IT Consulting</h3>
    <p>Veltana could offer IT consulting services to Private Banking clients, helping them optimize their existing IT infrastructure and develop strategies to improve efficiency, productivity, and security.</p>
  </div>
  <div class="service" style="left:470px;top:367px">
    <svg width="54" height="54" viewBox="0 0 54 54" fill="none" stroke="#1a5fc0" stroke-width="1.6"><rect x="18" y="4" width="18" height="16" rx="2"/><path d="M24 10l-3 2 3 2M30 10l3 2-3 2"/><path d="M4 30h16v16H4zM34 30h16v16H34z"/><path d="M27 20v6M12 30v-4h30v4"/></svg>
    <h3>Custom Solutions</h3>
    <p>Veltana could highlight their ability to provide customized solutions to meet their clients' unique needs and requirements.</p>
  </div>
  <div class="service" style="left:805px;top:367px">
    <svg width="54" height="56" viewBox="0 0 54 56" fill="none" stroke="#1a5fc0" stroke-width="1.6"><rect x="4" y="8" width="34" height="44" rx="2"/><path d="M14 4h14v8H14z"/><circle cx="21" cy="30" r="8"/><circle cx="21" cy="30" r="3"/><path d="M40 16l8 4-14 26-6 2 1-6z"/></svg>
    <h3>Project Management</h3>
    <p>Veltana could offer project management services to ensure their clients' IT projects are completed on time, within budget, and to the highest quality standards.</p>
  </div>

  <a class="btn">Contact now</a>
</section>

<section class="stats" role="img" aria-label="Dimmed office photo behind company figures">
  <div class="stat" style="left:58px;top:62px">
    <svg width="66" height="48" viewBox="0 0 66 48" fill="#4f9bff"><circle cx="22" cy="12" r="10"/><circle cx="46" cy="12" r="10"/><path d="M2 46c0-12 9-20 20-20s20 8 20 20zM28 46c0-12 8-20 18-20s18 8 18 20z"/></svg>
    <b>3258</b><span>Satisfied Clients</span>
  </div>
  <div class="stat" style="left:282px;top:58px">
    <svg width="52" height="52" viewBox="0 0 52 52" fill="none" stroke="#4f9bff" stroke-width="4"><circle cx="26" cy="28" r="18"/><path d="M26 18v10l7 5M6 10l8-6M46 10l-8-6"/></svg>
    <b>20</b><span>Years Of Experience</span>
  </div>
  <div class="stat" style="left:501px;top:62px">
    <svg width="66" height="48" viewBox="0 0 66 48" fill="none" stroke="#4f9bff" stroke-width="3"><path d="M14 3h38l12 14-31 28L2 17z"/><path d="M2 17h62M24 3l-6 14 15 28 15-28-6-14"/></svg>
    <b>140</b><span>Positive Solutions</span>
  </div>
  <div class="stat" style="left:713px;top:60px">
    <svg width="60" height="50" viewBox="0 0 60 50" fill="#4f9bff"><path d="M30 2 58 14v4H2v-4z"/><rect x="6" y="21" width="48" height="3"/><path d="M10 26h5v16h-5zM22 26h5v16h-5zM33 26h5v16h-5zM45 26h5v16h-5z"/><rect x="2" y="44" width="56" height="5"/></svg>
    <b>256</b><span>Partner Banks</span>
  </div>
  <div class="stat" style="left:933px;top:58px">
    <svg width="50" height="52" viewBox="0 0 50 52" fill="#4f9bff"><rect x="8" y="2" width="4" height="50"/><path d="M12 4c10-4 16 6 32 2l-6 12 6 12c-16 4-22-6-32-2z"/></svg>
    <b>3258</b><span>Businesses Growing</span>
  </div>
  <div class="abs stats-rule"></div>
  <div class="abs stats-cta">Not sure what you need?<br>Contact now</div>
</section>

<div class="contact-card call">
  <svg class="abs" style="left:43px;top:52px" width="62" height="62" viewBox="0 0 62 62" fill="none" stroke="#1a5fc0" stroke-width="2"><path d="M14 6l8 12-5 6c3 8 10 15 18 18l6-5 12 8-4 8c-2 3-6 4-10 3C22 50 10 38 4 20c-1-4 0-8 3-10z"/><path d="M36 12c7 1 12 6 13 13M36 4c11 1 20 10 21 21"/></svg>
  <div class="abs label">Call us now</div>
  <div class="abs number">+ 1 555-014-2283</div>
</div>
<div class="contact-card signup">
  <svg class="abs" style="left:43px;top:55px" width="60" height="60" viewBox="0 0 60 60" fill="none" stroke="#1a5fc0" stroke-width="2"><path d="M2 24l28-20 28 20v32H2z"/><path d="M2 24l28 20 28-20M2 56l20-18M58 56 38 38"/><rect x="14" y="12" width="32" height="22" fill="#fff"/><path d="M20 19h20M20 25h20"/></svg>
  <div class="abs label">Sign up for emails</div>
  <div class="abs field">Enter your email</div>
  <div class="abs field-btn"><svg width="18" height="16" viewBox="0 0 18 16" fill="none" stroke="#fff" stroke-width="2.4"><path d="M1 8h15M9 1l7 7-7 7"/></svg></div>
</div>

<section class="team">
  <div class="abs eyebrow">Our team</div>
  <h2 class="abs heading">Meet our team</h2>
  <div class="member" style="left:99px"><div class="portrait" role="img" aria-label="Portrait of a team member in a dark suit"></div><h3>Name Goes Here</h3><p>Designation Goes here</p><div class="socials"><i></i><i></i></div></div>
  <div class="member" style="left:354px"><div class="portrait" role="img" aria-label="Portrait of a team member in a dark suit"></div><h3>Name Goes Here</h3><p>Designation Goes here</p><div class="socials"><i></i><i></i></div></div>
  <div class="member" style="left:611px"><div class="portrait" role="img" aria-label="Portrait of a team member in a dark blazer"></div><h3>Name Goes Here</h3><p>Designation Goes here</p><div class="socials"><i></i><i></i></div></div>
  <div class="member" style="left:868px"><div class="portrait" role="img" aria-label="Portrait of a team member in a dark suit"></div><h3>Name Goes Here</h3><p>Designation Goes here</p><div class="socials"><i></i><i></i></div></div>
</section>

<section class="testimonials">
  <div class="abs eyebrow">Testimonial</div>
  <h2 class="abs heading">What client say?</h2>
  <div class="arrow" style="left:1013px"><svg width="18" height="14" viewBox="0 0 18 14" fill="none" stroke="#9aa3b0" stroke-width="2"><path d="M17 7H2M8 1 2 7l6 6"/></svg></div>
  <div class="arrow" style="left:1065px"><svg width="18" height="14" viewBox="0 0 18 14" fill="none" stroke="#17202e" stroke-width="2.4"><path d="M1 7h15M10 1l6 6-6 6"/></svg></div>
  <div class="quote" style="left:101px;width:487px">Dolor amet, consectetur adipiscing elit consequat elit. Mauris hendrerit fringilla ligula, nec congue leo pharetra in. Quisque commodo vehicula justo, tincidunt vehicula.</div>
  <div class="quote" style="left:615px;width:488px">Adipiscing elit consequat elit. Mauris hendrerit fringilla ligula, nec congue leo pharetra in. Quisque commodo vehicula justo, tincidunt vehicula consequat vel lorrem.</div>
  <div class="author" style="left:113px"><div class="avatar" role="img" aria-label="Client portrait" style="margin-left:0"></div><div><b>Marcus Dellow</b><small>Designation</small></div></div>
  <div class="author" style="left:627px"><div class="avatar" role="img" aria-label="Client portrait" style="margin-left:0"></div><div><b>Marcus Dellow</b><small>Designation</small></div></div>
</section>

<footer class="site-footer">
  <div class="abs brand">Veltana</div>
  <div class="abs foot-social"><i></i><i></i><i></i><i></i></div>
  <div class="abs foot-rule" style="top:101px"></div>
  <div class="foot-col" style="left:100px"><h4>COMPANY</h4><ul><li>Who we are</li><li>Services</li><li>Team</li><li>Contact us</li><li>Faq</li></ul></div>
  <div class="foot-col" style="left:357px"><h4>SERVICES</h4><ul><li>Software Development</li><li>Cybersecurity</li><li>Data Analytics</li><li>IT Consulting</li><li>Custom Solutions</li><li>Project Management</li></ul></div>
  <div class="foot-col" style="left:624px"><h4>QUICK LINKS</h4><ul><li>Blog</li><li>Privacy polly</li><li>Support</li><li>Latest News</li></ul></div>
  <div class="foot-col" style="left:872px"><h4>CONTACT INFO</h4><ul class="contact"><li>Address : 8 Rue des Alpes, 1201 Geneva, Switzerland</li><li>Phone : +41 (22) 555 0147</li><li>Email : <a>support@veltana.com</a></li><li>Fax : +41 (22) 555 0148</li></ul></div>
  <div class="abs foot-rule" style="top:388px"></div>
  <div class="abs copy">© 2023 Veltana.com. All rights reserved.</div>
</footer>

</body>
</html>
```